A modern, fresh introduction to Buddhism

I need a book cover for an A6 sized book to be used both for ebook and hard copy. The author is a young, modern Buddhist teacher of high standing who has written this short intro to Buddhism in an informal Q & As format using modern, accessible language to convey profound and meaningful ideas to the general public. The author is Tibetan, but teaches worldwide and is very personable and dynamic. The cover should portray this and have a fresh yet authentic feel to it (nothing new-agey!). Please see the author's websites www.norvalemtasheteacher.org and www.pwrt.org for reference, but do not feel that the design must align completely with the website designs.

Target Market(s)

General public both in Europe and America and in Asia ranging from teenagers to the elderly. A really broad audience.

Industry/Entity Type

Teacher

Requirements
Must have
• Please include the following text that on the front cover:

A Window onto Stillness

By Drawa Tsomen Lhundrup

Please include the following on the back cover:

Yunor Trenpa Publications (with attached logo above it)
Nice to have
• A simplistic, artistic, and modern look without any traditional religious images.
Should not have
• No buddha images or religious images. I would prefer a more simplistic, modern and artistic look.

```html
<!DOCTYPE html>
<html lang="en">
<head>
<meta charset="utf-8">
<title>A Window onto Stillness — Cover</title>
<link rel="stylesheet" href="https://fonts.googleapis.com/css2?family=Montserrat:wght@500;700&display=swap">
<style>
  :root {
    --ink: #050404;
    --title-red: #c8311f;
    --line-red: #b8402c;
    --byline-grey: #9a8f8a;
    --smoke-violet: #b56ab8;
    --smoke-pink: #d7587a;
    --smoke-rust: #8a2a14;
    --smoke-amber: #e99a2c;
    --smoke-gold: #f6d27a;
  }
  html, body {
    margin: 0;
    padding: 0;
    width: 783px;
    height: 1200px;
    overflow: hidden;
    background: var(--ink);
  }
  .cover {
    position: relative;
    width: 783px;
    height: 1200px;
    background: var(--ink);
    overflow: hidden;
    font-family: "Montserrat", Arial, sans-serif;
  }
  .smoke-field {
    position: absolute;
    left: 0;
    top: 360px;
    width: 783px;
    height: 840px;
    background:
      radial-gradient(ellipse 260px 180px at 150px 560px, rgba(215, 88, 122, 0.75), transparent 70%),
      radial-gradient(ellipse 300px 220px at 230px 700px, rgba(181, 106, 184, 0.7), transparent 72%),
      radial-gradient(ellipse 200px 160px at 60px 420px, rgba(200, 60, 40, 0.55), transparent 70%),
      radial-gradient(ellipse 280px 240px at 680px 760px, rgba(246, 210, 122, 0.7), transparent 70%),
      radial-gradient(ellipse 300px 260px at 600px 620px, rgba(233, 154, 44, 0.6), transparent 72%),
      radial-gradient(ellipse 360px 200px at 420px 320px, rgba(138, 42, 20, 0.45), transparent 75%),
      radial-gradient(ellipse 260px 200px at 400px 820px, rgba(120, 60, 130, 0.5), transparent 72%);
  }
  .emblem {
    position: absolute;
    left: 136px;
    top: 22px;
    width: 500px;
    height: 500px;
  }
  .emblem-figure {
    position: absolute;
    left: 80px;
    top: 40px;
    width: 340px;
    height: 400px;
    border-radius: 170px 170px 60px 60px;
    background: radial-gradient(ellipse at 50% 45%, rgba(150, 45, 30, 0.35), rgba(60, 15, 10, 0.15) 70%, transparent);
  }
  .title {
    position: absolute;
    left: 0;
    right: 0;
    top: 545px;
    margin: 0;
    text-align: center;
    color: var(--title-red);
    font-weight: 700;
    font-size: 31px;
    letter-spacing: 0.5px;
    text-transform: uppercase;
    white-space: nowrap;
  }
  .byline {
    position: absolute;
    right: 78px;
    top: 600px;
    margin: 0;
    color: var(--byline-grey);
    font-weight: 500;
    font-size: 15px;
    letter-spacing: 2.4px;
    text-transform: uppercase;
    white-space: nowrap;
  }
</style>
</head>
<body>
  <main class="cover">
    <div class="smoke-field" role="img" aria-label="Abstract flowing smoke ribbons in violet and pink on the left and amber and gold on the right"></div>

    <div class="emblem">
      <div class="emblem-figure" role="img" aria-label="Fine red line drawing of a seated figure beneath an arch"></div>
      <svg width="500" height="500" viewBox="0 0 500 500" aria-hidden="true">
        <circle cx="250" cy="250" r="248" fill="none" stroke="var(--line-red)" stroke-width="2"/>
      </svg>
    </div>

    <h1 class="title">A Window onto Stillness</h1>
    <p class="byline">By Drawa Tsomen Lhundrup</p>
  </main>
</body>
</html>
```